Shiatsu in der Kindlichen Entwicklung
Zielgruppe
Frauen, Familien
Aufgabenstellung
Es sollte ein buntes, gemaltes (Buntstift) aber trotzedem elegantes und ansprechendes Desigen haben.
Ich stelle mir einen Flyer vor, der ein Cover hat und kombinierbare einzelnen Seiten, die man dazu stecken kann. Je nach Interesse meiner Kunden.
Jedes Thema hat eine eigene Seite: Shiatsu in der Schwangerschaft, Baby Shiatsu und Kinder Shiatsu, Shiatsu in der Schule, Shiatsu Kurse usw. die dem Flyer beigefügt werden können.
Ich begleite Famielien und Kinder von klein bis gross.
Es sollten drei Abschnitte sein:
1. Shiatsu in der Schwangerschaft
2. Baby Shiatsu
3. Shiatsu mit Kindern

```html
<!DOCTYPE html>
<html lang="de">
<head>
<meta charset="utf-8">
<title>Shiatsu Flyer – Berenike Pohl</title>
<link rel="stylesheet" href="https://fonts.googleapis.com/css2?family=Amatic+SC:wght@700&family=Ubuntu:wght@400;500&family=Arimo:wght@700&display=swap">
<style>
  :root{
    --green:#5bbd75;
    --green-soft:#82c47c;
    --pink:#d396c5;
    --pink-text:#c987bd;
    --orange:#ef7b56;
    --text:#4a4a4a;
    --white:#ffffff;
    --bg:#ffffff;
    --cyan:#3cc6e0;
    --red:#e8425a;
  }
  *{margin:0;padding:0;box-sizing:border-box}
  html,body{width:1059px;height:1200px;overflow:hidden;background:var(--bg)}
  body{position:relative;font-family:"Ubuntu",sans-serif;color:var(--text)}
  .label{position:absolute;font-family:"Arimo",Arial,sans-serif;font-weight:700;font-size:13.5px;color:#111}
  .label--cover{left:143px;top:280px}
  .label--back{left:840px;top:293px}
  .label--sheets{left:0;width:1059px;text-align:center;top:1153px}

  .panel{position:absolute;width:249px;height:497px;background:var(--white);overflow:hidden;
    box-shadow:0 1px 4px rgba(0,0,0,.28)}
  .panel__head{position:absolute;left:0;top:0;width:100%;display:flex;align-items:center;justify-content:center;
    text-align:center;color:var(--white);font-family:"Amatic SC",cursive;font-weight:700;line-height:1.05}
  .panel__photo{position:absolute;left:0;width:100%}
  .panel__rule{position:absolute;left:0;width:100%;height:3px}
  .panel__text{position:absolute;left:30px;font-size:7.6px;line-height:10px}
  .panel__subhead{position:absolute;left:30px;font-family:"Amatic SC",cursive;font-weight:700;font-size:24px;line-height:1}
  .panel__list{position:absolute;left:28px;list-style:none;font-size:7.6px;line-height:12.5px}
  .panel__list li{padding-left:5px;text-indent:-5px}
  .panel__list li::before{content:"•";margin-right:2px}
  .ornament{position:absolute;border-radius:50%}

  /* cover */
  .cover{left:244px;top:33px}
  .cover .panel__head{height:90px;background:var(--green);font-size:34px}
  .cover__name{position:absolute;left:0;width:100%;top:137px;text-align:center;font-family:"Amatic SC",cursive;
    font-weight:700;font-size:28px;color:var(--green);letter-spacing:.5px}
  .cover__roles{position:absolute;left:0;width:100%;top:172px;text-align:center;font-size:7.6px;line-height:10.4px}
  .cover__drawing{top:262px;height:235px;
    background:linear-gradient(180deg,#fdf6e6 0%,#cfe6f4 30%,#a9d3ee 45%,#f4e3d3 62%,#e6d9ee 74%,#b6e07f 88%,#8fcf55 100%)}

  /* back */
  .back{left:564px;top:33px;background:var(--green)}
  .back__title{position:absolute;left:0;width:100%;top:44px;text-align:center;color:var(--white);
    font-family:"Amatic SC",cursive;font-weight:700;font-size:26px}
  .back__claim{position:absolute;left:0;width:100%;top:80px;text-align:center;color:var(--white);font-size:7.4px;line-height:10.4px}

  /* supplement sheets */
  .pregnancy{left:86px;top:631px}
  .pregnancy .panel__head{height:79px;background:var(--green-soft);font-size:26px}
  .pregnancy .panel__photo{top:79px;height:130px;background:linear-gradient(160deg,#f4e6de 0%,#e9c3ad 45%,#f7f1ee 100%)}
  .pregnancy .panel__rule{top:209px;background:var(--green-soft)}
  .pregnancy .panel__text{top:226px;width:185px}
  .pregnancy .panel__subhead{top:339px;color:var(--green-soft)}
  .pregnancy .panel__list{top:371px;width:200px}

  .baby{left:391px;top:631px}
  .baby .panel__head{height:57px;background:var(--pink);font-size:28px}
  .baby .panel__photo{top:57px;height:151px;background:linear-gradient(150deg,#fbf7f5 0%,#f0d5c6 45%,#e8e3df 100%)}
  .baby .panel__rule{top:208px;background:var(--pink)}
  .baby .panel__text{top:226px;width:186px}
  .baby .panel__subhead{top:309px;color:var(--pink-text)}
  .baby .panel__list{top:342px;width:200px}

  .kids{left:707px;top:631px}
  .kids .panel__head{height:57px;background:var(--orange);font-size:28px}
  .kids .panel__photo{top:57px;height:149px;background:linear-gradient(150deg,#e7e9ea 0%,#d9c8bc 50%,#eef0f0 100%)}
  .kids .panel__rule{top:206px;background:var(--orange)}
  .kids .panel__text{top:224px;width:186px;line-height:12.4px}
  .kids .panel__subhead{top:290px;color:var(--orange)}
  .kids .panel__list{top:322px;width:160px}
</style>
</head>
<body>

<div class="label label--cover">Cover Flyer</div>
<div class="label label--back">Rückseite Flyer</div>

<!-- Cover -->
<section class="panel cover">
  <div class="panel__head">TCM &amp; SHIATSU</div>
  <div class="ornament" role="img" aria-label="Schmetterling-Ornament in Rot und Grün" style="left:10px;top:78px;width:80px;height:52px;background:rgba(232,66,90,.16)"></div>
  <div class="cover__name">Berenike Pohl</div>
  <div class="cover__roles">Dipl. Shiatsu-Therapeutin<br>lumeo Baby und Kinder Shiatsu Therapeutin<br>Dorn Therapeutin</div>
  <div class="panel__photo cover__drawing" role="img" aria-label="Buntstiftzeichnung einer Familie unter einem Regenbogen mit Wolken, Sonne, Blumen und Wiese"></div>
</section>

<!-- Back -->
<section class="panel back">
  <div class="back__title">SHIATSU</div>
  <div class="back__claim">Jahrtausende alte fernöstliche Medizin, verknüpft<br>mit dem Wissen der modernen Medizin.</div>
  <div class="ornament" role="img" aria-label="Weißes Schmetterling-Ornament mit gepunkteter Flugbahn" style="left:10px;top:398px;width:86px;height:68px;background:rgba(255,255,255,.16)"></div>
</section>

<!-- Pregnancy -->
<section class="panel pregnancy">
  <div class="panel__head">SHIATSU IN DER<br>SCHWANGERSCHAFT</div>
  <div class="panel__photo" role="img" aria-label="Foto eines Babybauchs mit darauf liegenden Händen"></div>
  <div class="panel__rule"></div>
  <p class="panel__text">Wussten Sie, dass Shiatsu eine wunderbare Methode ist während der Schwangerschaft? Es wirkt unterstützend, begleitend, geburts-vorbereitend und sehr entspannend. Diese Ruhe gibt den nötigen Raum, den oftmals kräfteraubenden Alltag auszublenden und wieder in den eigenen Körper zu lauschen. Dabei findet eine natürliche und innige Verbindung mit dem Baby statt. Das ist kraftspendend und harmonisierend.</p>
  <div class="ornament" role="img" aria-label="Schmetterling-Ornament in Orange und Grün mit gepunkteter Flugbahn" style="left:166px;top:380px;width:76px;height:54px;background:rgba(239,123,86,.14)"></div>
  <div class="panel__subhead">ANWENDUNG</div>
  <ul class="panel__list">
    <li>Morgendlicher Übelkeit</li>
    <li>Rückenschmerzen</li>
    <li>Wassereinlagerungen</li>
    <li>Schlafprobleme</li>
    <li>Freude</li>
    <li>Sorge</li>
    <li>Ängste</li>
    <li>Erfahrungen vorangegangener Geburten</li>
    <li>Partnerübungen für alle Phasen der Geburt</li>
  </ul>
</section>

<!-- Baby -->
<section class="panel baby">
  <div class="panel__head">BABY SHIATSU</div>
  <div class="panel__photo" role="img" aria-label="Foto eines liegenden Babys, das sanft von Händen massiert wird"></div>
  <div class="panel__rule"></div>
  <div class="ornament" role="img" aria-label="Schmetterling-Ornament in Türkis und Lila mit gepunkteter Flugbahn" style="left:22px;top:50px;width:76px;height:52px;background:rgba(60,198,224,.16)"></div>
  <p class="panel__text">Auf diese angenehme und sanfte Behandlung sprechen gerade Babys mit ihren feinsinnigen Empfindungen besonders gut an. Speziell für sie wurde lumeo•Baby Shiatsu® entwickelt, dass ausdrücklich auf die Bedürfnisse und Wünsche der Kleinsten eingeht und sie in der Entwicklung fördert.</p>
  <div class="panel__subhead">VORTEILE</div>
  <ul class="panel__list">
    <li>unterstützt die Entwicklung des Kindes</li>
    <li>vertieft den Kontakt und stärkt die Bindung von Mutter und Baby</li>
    <li>hilfreich bei Schlafstörungen, Blähungen, etc.</li>
    <li>kann selbst erlernt &amp; zuhause umgesetzt werden</li>
    <li>richtet das Baby durch Streicheleinheiten auf</li>
    <li>ist gut für die Haltung, Gesundheit und emotionale Stabilität</li>
    <li>optimiert die Wahrnehmung</li>
  </ul>
</section>

<!-- Kids -->
<section class="panel kids">
  <div class="panel__head">SHIATSU MIT KINDERN</div>
  <div class="panel__photo" role="img" aria-label="Foto eines Mädchens mit pinker Blume in einem weißen Korbsessel"></div>
  <div class="panel__rule"></div>
  <p class="panel__text">Kirin Programm ist ein Schulprogramm für Primarschüler und Kinder bis zum Alter von etwa zwölf Jahren. Es setzt sich zusammen aus der Behandlungssequenz Kirin-Shiatsu.</p>
  <div class="ornament" role="img" aria-label="Schmetterling-Ornament in Grün und Orange mit gepunkteter Flugbahn" style="left:142px;top:405px;width:100px;height:70px;background:rgba(91,189,117,.14)"></div>
  <div class="panel__subhead">ZIELE</div>
  <ul class="panel__list">
    <li>die Gesundheit zu fördern</li>
    <li>die Konzentrationsfähigkeit zu verbessern</li>
    <li>eine gesunde Haltung zu unterstützen</li>
    <li>das Klassenklima zu verbessern</li>
    <li>die Selbstwirksamkeit zu verbessern</li>
    <li>ist eine Einführung in die japanische Kultur und Sprache</li>
    <li>und macht Alt und Jung riesen grossen Spass</li>
  </ul>
</section>

<div class="label label--sheets">Zusatzblätter</div>

</body>
</html>
```